ARC VOLLEY Business Card Project

I'd like to request a business card design for the new company I've launched.
The name of the company is "ARC VOLLEY" an indoor unmanned tennis practice facility.
We would like to see designs that use our brand identity color in the logo I've attached.
We hope to get the design with modern, luxurious and elegant tone and manner.
We hope the logo should not be too big.

Business card must have elements as below:
- Logo (One of the logos I've attached)
- Name (In Korean Text) : 박 서 윤
- Title (In Korean Text) : 대표
- Phone Number : 010-8472-3916
- Email Address : seoyun.park@arcvolley-example.co.kr
- Website : www.arcvolley-example.co.kr
- Instagram : arcvolley
- Address (In Korean text) : 경기도 용인시 수지구 풍덕천로 456 미래타워 5층 501호, 502호

Target Market(s)

Tennis amateurs in 20 to 40s

Industry/Entity Type

Sports, Hobby

Contact Information for Business Card

- Logo (One of the logos I've attached) - Name (In Korean Text) : 박 서 윤 - Title (In Korean Text) : 대표 - Phone Number : 010-8472-3916 - Email Address : seoyun.park@arcvolley-example.co.kr - Website : www.arcvolley-example.co.kr - Instagram : arcvolley - Address (In Korean text) : 경기도 용인시 수지구 풍덕천로 456 미래타워 5층 501호, 502호

Font styles to use
Sans Serif

Requirements
Must have
• Double sided
Nice to have
• Logo with intaglio or relief embossing
Should not have
• Logo should not be too big.

```html
<!DOCTYPE html>
<html lang="ko">
<head>
<meta charset="utf-8">
<title>ARC VOLLEY Business Card</title>
<link href="https://fonts.googleapis.com/css2?family=Cinzel:wght@500&family=Noto+Serif+KR:wght@400;500&display=swap" rel="stylesheet">
<style>
  :root {
    --backdrop: #e9eae9;
    --card-green: #1f4a2c;
    --card-green-deep: #173a22;
    --emboss-green: #2d7d41;
    --emboss-light: #3fa657;
    --silver: #eef1ee;
    --silver-soft: #c9d3cb;
    --rule: #9fb2a4;
  }
  * { margin: 0; padding: 0; box-sizing: border-box; }
  html, body { width: 1200px; height: 802px; overflow: hidden; }
  body {
    background: var(--backdrop);
    display: flex;
    align-items: center;
    justify-content: center;
    gap: 44px;
  }
  .card {
    position: relative;
    width: 520px;
    height: 289px;
    background: linear-gradient(160deg, var(--card-green) 0%, var(--card-green-deep) 100%);
    color: var(--silver);
    overflow: hidden;
  }
  .wordmark {
    position: absolute;
    font-family: "Cinzel", serif;
    font-weight: 500;
    letter-spacing: 0.04em;
    color: var(--silver);
    white-space: nowrap;
  }
  .wordmark-rule { position: absolute; height: 1px; background: var(--rule); }

  /* front */
  .front .brand-dot {
    position: absolute; left: 38px; top: 46px;
    width: 40px; height: 40px; border-radius: 50%;
    background: var(--silver);
  }
  .front .wordmark { left: 92px; top: 46px; font-size: 30px; line-height: 40px; }
  .front .wordmark-rule { left: 92px; top: 92px; width: 214px; }
  .person {
    position: absolute; left: 150px; top: 132px;
    font-family: "Noto Serif KR", serif; text-align: center;
  }
  .person-name { font-size: 16px; letter-spacing: 0.1em; }
  .person-title { font-size: 11px; color: var(--silver-soft); margin-top: 4px; }
  .divider {
    position: absolute; left: 270px; top: 124px;
    width: 1px; height: 82px; background: var(--rule);
  }
  .contacts {
    position: absolute; left: 282px; top: 124px;
    list-style: none;
    font-family: "Noto Serif KR", serif; font-size: 10px;
    color: var(--silver);
  }
  .contacts li { display: flex; align-items: center; gap: 7px; height: 20.5px; }
  .contacts svg { width: 11px; height: 11px; flex: none; }
  .address {
    position: absolute; left: 38px; top: 222px;
    font-family: "Noto Serif KR", serif; font-size: 11px; line-height: 19px;
    color: var(--silver-soft);
  }

  /* back */
  .back .emblem {
    position: absolute; left: 42px; top: 52px;
    width: 190px; height: 190px; border-radius: 50%;
    background: radial-gradient(circle at 38% 35%, var(--emboss-light) 0%, var(--emboss-green) 55%, #1d5a2e 100%);
    box-shadow: inset 2px 3px 6px rgba(0,0,0,0.35), 0 1px 0 rgba(255,255,255,0.08);
  }
  .back .wordmark { left: 262px; top: 128px; font-size: 30px; line-height: 40px; }
  .back .wordmark-rule { left: 262px; top: 174px; width: 214px; }
</style>
</head>
<body>
  <section class="card front" aria-label="Card front">
    <div class="brand-dot"></div>
    <div class="wordmark">ARC VOLLEY</div>
    <div class="wordmark-rule"></div>

    <div class="person">
      <div class="person-name">박 서 윤</div>
      <div class="person-title">대표</div>
    </div>

    <div class="divider"></div>
    <ul class="contacts">
      <li>
        <svg viewBox="0 0 12 12"><circle cx="6" cy="6" r="5.5" fill="var(--silver)"/><path d="M4 3.2l1 1.4-.6.7c.4.9 1 1.5 1.9 1.9l.7-.6 1.4 1-.6 1.2C5.9 8.6 3.4 6.1 3.2 3.8z" fill="var(--card-green)"/></svg>
        010-8472-3916
      </li>
      <li>
        <svg viewBox="0 0 12 12"><rect x="0.5" y="2" width="11" height="8" fill="var(--silver)"/><path d="M1 2.6l5 4 5-4" fill="none" stroke="var(--card-green)" stroke-width="1"/></svg>
        seoyun.park@arcvolley-example.co.kr
      </li>
      <li>
        <svg viewBox="0 0 12 12"><circle cx="6" cy="6" r="5.5" fill="var(--silver)"/><path d="M6 .8v10.4M.8 6h10.4M6 .8c-2.6 2.8-2.6 7.6 0 10.4M6 .8c2.6 2.8 2.6 7.6 0 10.4" fill="none" stroke="var(--card-green)" stroke-width=".8"/></svg>
        www.arcvolley-example.co.kr
      </li>
      <li>
        <svg viewBox="0 0 12 12"><rect x="0.5" y="0.5" width="11" height="11" rx="2.5" fill="var(--silver)"/></svg>
        arcvolley
      </li>
    </ul>

    <p class="address">경기도 용인시 수지구 풍덕천로 456<br>미래타워 5층 501호, 502호</p>
  </section>

  <section class="card back" aria-label="Card back">
    <div class="emblem"></div>
    <div class="wordmark">ARC VOLLEY</div>
    <div class="wordmark-rule"></div>
  </section>
</body>
</html>
```